Range of Mayonise Bottles

We are wanting a Logo and Artwork for a Range of Mayonnaise’s.
There are 3 lines in total
Mayonnaise Regular
Mayonnaise and Garlic
Aioli ( Mayo and Lemon)
All 300g Upside down Style Bottle.
Image attached.
Logo: is Brindle Pantry

Target Market(s)

Supermarket Line

Requirements
Must have
• Brindle Pantry must be on all 3 lines
Pictures on Front
weight on Front
Ingredinets Only English
we will provide Nutrtioanl Info so please leave space
Barcodes I will upload
Nice to have
• Image of Mayonaise

```html
<!DOCTYPE html>
<html lang="en">
<head>
<meta charset="utf-8">
<title>Brindle Pantry Garlic Mayonnaise Label</title>
<link rel="stylesheet" href="https://fonts.googleapis.com/css2?family=Anton&family=Russo+One&family=Open+Sans:wght@600;700&display=swap">
<style>
  :root {
    --page-bg: #f4f4f5;
    --label-bg: #e3e3e6;
    --label-edge: #d2d2d6;
    --brand-green: #4f9a1f;
    --band-green: #22a33c;
    --band-green-light: #3fc458;
    --band-silver: #c9cacd;
    --ink: #222222;
    --badge-green: #7cbf3a;
    --white: #ffffff;
  }
  * { margin: 0; padding: 0; box-sizing: border-box; }
  html, body { width: 1200px; height: 1151px; overflow: hidden; background: var(--page-bg); }
  .canvas { position: relative; width: 1200px; height: 1151px; }
  .label { position: absolute; left: 295px; top: 150px; width: 611px; height: 848px; }
  .label-shape { position: absolute; inset: 0; }
  .brand {
    position: absolute; left: 0; width: 100%; top: 92px; text-align: center;
    font-family: "Anton", sans-serif; color: var(--brand-green);
    font-size: 76px; line-height: 0.95; letter-spacing: 1px;
  }
  .band { position: absolute; inset: 0; }
  .product-name, .product-flavour {
    position: absolute; font-family: "Russo One", sans-serif; color: var(--white);
    transform: rotate(-5deg); white-space: nowrap; transform-origin: center;
  }
  .product-name { left: 100px; top: 318px; font-size: 62px; letter-spacing: 2px; }
  .product-flavour { left: 215px; top: 393px; font-size: 50px; letter-spacing: 2px; }
  .food-photo {
    position: absolute; left: 139px; top: 472px; width: 344px; height: 216px;
    border-radius: 40px 40px 60px 60px;
    background: radial-gradient(ellipse at 50% 60%, #d9a23a 0%, #c7652b 35%, #62b234 70%, rgba(98,178,52,0) 100%);
  }
  .garlic-illustration {
    position: absolute; left: 285px; top: 652px; width: 180px; height: 186px;
    border-radius: 50% 50% 46% 46% / 38% 38% 62% 62%;
    background: radial-gradient(circle at 50% 60%, #f6f6f6 0%, #d4d4d4 75%, #bdbdbd 100%);
  }
  .nutrition { position: absolute; left: 83px; top: 536px; width: 54px; }
  .badge {
    width: 54px; height: 72px; margin-bottom: 5px; background: var(--badge-green);
    border-radius: 14px; text-align: center; font-family: "Open Sans", sans-serif;
    color: var(--ink); padding-top: 4px;
  }
  .badge-label { font-size: 10px; font-weight: 600; display: block; }
  .badge-value { font-size: 16px; font-weight: 700; display: block; line-height: 1.2; }
  .badge-percent {
    display: inline-block; margin-top: 3px; background: var(--white); border-radius: 10px;
    font-size: 12px; font-weight: 700; padding: 1px 6px;
  }
  .net-volume {
    position: absolute; left: 147px; top: 805px; font-family: "Open Sans", sans-serif;
    font-weight: 700; font-size: 26px; color: var(--ink);
  }
</style>
</head>
<body>
<div class="canvas">
  <div class="label">
    <svg class="label-shape" viewBox="0 0 611 848" width="611" height="848">
      <path d="M40 0 H571 Q611 0 605 40 Q590 220 575 330 Q565 420 585 560 Q611 760 605 808 Q601 848 561 848 H50 Q10 848 6 808 Q0 760 26 560 Q46 420 36 330 Q21 220 6 40 Q0 0 40 0 Z"
            fill="var(--label-bg)" stroke="var(--label-edge)" stroke-width="2"/>
    </svg>
    <div class="brand">Brindle<br>Pantry</div>
    <svg class="band" viewBox="0 0 611 848" width="611" height="848">
      <defs>
        <linearGradient id="bandGreen" x1="0" y1="0" x2="1" y2="0">
          <stop offset="0" stop-color="var(--band-green)"/>
          <stop offset="0.5" stop-color="var(--band-green-light)"/>
          <stop offset="1" stop-color="var(--band-green)"/>
        </linearGradient>
      </defs>
      <polygon points="34,316 577,250 577,268 34,334" fill="var(--band-silver)"/>
      <polygon points="34,334 577,268 575,466 30,514" fill="url(#bandGreen)"/>
    </svg>
    <div class="product-name">MAYONNAISE</div>
    <div class="product-flavour">GARLIC</div>
    <div class="food-photo" role="img" aria-label="Photo of salads and wraps with lettuce and mayonnaise"></div>
    <div class="garlic-illustration" role="img" aria-label="Line drawing of a garlic bulb"></div>
    <div class="nutrition">
      <div class="badge"><span class="badge-label">Fat</span><span class="badge-value">8.4g</span><span class="badge-percent">12%</span></div>
      <div class="badge"><span class="badge-label">Sugar</span><span class="badge-value">19.2g</span><span class="badge-percent">21%</span></div>
      <div class="badge"><span class="badge-label">Calories</span><span class="badge-value">150</span><span class="badge-percent">8%</span></div>
      <div class="badge"><span class="badge-label">Saturates</span><span class="badge-value">2.9g</span><span class="badge-percent">15%</span></div>
    </div>
    <div class="net-volume">300 ml</div>
  </div>
</div>
</body>
</html>
```